PWRPT design for Company

Project: Develop a pwrpt for KL7ux. This can be just a blank pwrpt with standard templates that we can use to build our content and solutions around.
Website: www.kl7ux.example
Color Pallet: Try to use the color schema from our website.
PWRPT Design Tips: While we are a research-based company, our primary target is schools and school districts. We say our work is RESEARCH, POLICY, AND PRACTICE. I would like images that represent “WHY” our research matters, i.e. students, teachers, and administrators. If you can use images and stock photos that represent students with diverse backgrounds, teachers that are diverse and clearly teaching, and administrators that run a school, university, etc. We are in the process of updating our website, but the color scheme will remain the same.
Additional Information:
We built, researched, and designed, www.pvra-tq.example .
We built, researched, and designed, http://87wkgamma.example/olav/index.html
Target Market(s)
EDUCATION
Industry/Entity Type
It Company
Look and feel

```html
<!DOCTYPE html>
<html lang="en">
<head>
<meta charset="utf-8">
<title>KL7ux Presentation Template</title>
<link href="https://fonts.googleapis.com/css2?family=Lato:wght@300;400;700&display=swap" rel="stylesheet">
<style>
:root{
  --sky:#9dc3e6;
  --orange:#f4502a;
  --orange-soft:#f7845f;
  --ink:#333333;
  --muted:#8a8a8a;
  --panel:#efefef;
}
*{margin:0;padding:0;box-sizing:border-box}
html,body{width:800px;height:1200px;overflow:hidden;background:var(--sky);font-family:'Lato',sans-serif;color:var(--ink)}
.canvas{position:relative;width:800px;height:1200px}
.slide{position:absolute;width:355px;height:200px;background:#fff;overflow:hidden}
.col-a{left:32px}.col-b{left:417px}
.row-1{top:45px}.row-2{top:288px}.row-3{top:518px}.row-4{top:750px}.row-5{top:974px}

.brand{display:flex;align-items:center;gap:4px;font-weight:300;color:#555}
.brand-dot{border-radius:50%;background:var(--orange)}

.header-bar{position:absolute;top:7px;left:0;width:300px;height:17px;background:var(--orange);color:#fff;font-size:11px;line-height:17px;padding-left:6px}
.header-brand{position:absolute;top:9px;left:306px}
.header-brand .brand{font-size:9px}
.header-brand .brand-dot{width:7px;height:7px}

.photo{position:absolute}
.body-text{font-size:5.4px;line-height:6.6px}
.body-text p+p{margin-top:5px}

/* title slide */
.title-brand{position:absolute;left:20px;top:26px}
.title-brand .brand{font-size:19px}
.title-brand .brand-dot{width:14px;height:14px}
.title-band{left:0;top:80px;width:355px;height:88px;background:linear-gradient(90deg,#d9b9a4 0%,#f08a62 55%,var(--orange-soft) 100%)}
.title-text{position:absolute;right:22px;top:96px;color:#fff;font-size:14px;line-height:17px;text-align:right}
.title-foot{position:absolute;left:0;top:174px;width:355px;height:26px;background:var(--orange)}

/* research slide */
.rpp-photo{left:0;top:0;width:355px;height:200px;background:linear-gradient(135deg,#f1f2f3,#dcdfe2 60%,#c9ccce)}
.rpp-band{position:absolute;left:0;top:63px;width:190px;height:64px;background:rgba(244,80,42,.88)}
.rpp-text{position:absolute;left:30px;top:67px;color:#fff;font-size:15px;line-height:19px;text-align:center;width:95px}
.rpp-circle{position:absolute;left:133px;top:73px;width:44px;height:44px;border-radius:50%;background:#fff;opacity:.9}

/* welcome slide */
.welcome-photo{left:0;top:0;width:355px;height:160px;background:linear-gradient(180deg,#8f8f8f,#5a5a5a 60%,#474747)}
.welcome-box{position:absolute;left:112px;top:48px;width:130px;height:40px;border:2px solid #bdbdbd;background:rgba(255,255,255,.8);font-size:17px;text-align:center;line-height:36px;color:#222}
.welcome-brand{position:absolute;left:0;width:355px;top:168px;display:flex;justify-content:center}
.welcome-brand .brand{font-size:19px}
.welcome-brand .brand-dot{width:13px;height:13px}

/* about */
.about-text{position:absolute;left:44px;top:46px;width:246px}

/* leadership */
.lead-panel{position:absolute;left:0;top:36px;width:355px;height:138px;background:var(--panel)}
.lead-photo{left:21px;top:68px;width:69px;height:69px;border:3px solid var(--orange);background:linear-gradient(160deg,#7a5a48,#3a2a24)}
.lead-name{position:absolute;left:114px;top:47px;font-size:8.5px}
.lead-text{position:absolute;left:114px;top:64px;width:196px;font-size:5.1px;line-height:6.3px}

/* services */
.service{position:absolute;left:45px;display:flex;gap:12px;width:300px}
.service-icon{flex:none;width:27px;height:27px;border-radius:50%;background:var(--orange);border:3px solid #fde0d6;display:flex;align-items:center;justify-content:center}
.service-title{font-size:5.6px;font-weight:700;margin:1px 0 2px}
.service-text{font-size:5px;line-height:6px;width:225px}

/* overview */
.overview-text{position:absolute;left:15px;top:30px;width:152px;font-size:5px;line-height:6.2px}
.ov-library{left:180px;top:28px;width:156px;height:72px;background:linear-gradient(180deg,#a47c5a,#6b4a34)}
.ov-teacher{left:180px;top:112px;width:75px;height:73px;background:linear-gradient(180deg,#cfd3d6,#8d8f92)}
.ov-class{left:262px;top:112px;width:74px;height:73px;background:linear-gradient(180deg,#a9b7c4,#7b6c5e)}

/* chart */
.chart-box{position:absolute;left:19px;top:42px;width:198px;height:137px;border:1px solid #e4e4e4}
.points{position:absolute;left:229px;top:46px;width:115px}
.point{margin-bottom:11px}
.point-title{font-size:6.3px;color:var(--orange)}
.point-text{font-size:4.1px;line-height:5px;color:var(--muted)}

/* research list */
.study{position:absolute;top:39px;width:74px;display:flex;flex-direction:column;align-items:center}
.study-title{font-size:4.7px;font-weight:700;text-align:center;margin:4px 0 3px;line-height:5.6px}
.study-list{list-style:none;font-size:4.4px;line-height:5.3px;width:70px}
.study-list li{padding-left:6px;position:relative}
.study-list li::before{content:"\2713";position:absolute;left:0;color:#555}

/* contact */
.contact-brand{position:absolute;left:0;width:355px;top:48px;display:flex;justify-content:center}
.contact-brand .brand{font-size:22px}
.contact-brand .brand-dot{width:15px;height:15px}
.contact-row{position:absolute;left:130px;display:flex;align-items:center;gap:10px;font-size:6px;line-height:7px}
</style>
</head>
<body>
<div class="canvas">

  <section class="slide col-a row-1">
    <div class="title-brand"><div class="brand"><span class="brand-dot"></span>KL7ux</div></div>
    <div class="photo title-band" role="img" aria-label="Photo of a diverse team of smiling educators and administrators"></div>
    <div class="title-text">PRESENTATION<br>TITLE<br>HERE</div>
    <div class="title-foot"></div>
  </section>

  <section class="slide col-b row-1">
    <div class="photo rpp-photo" role="img" aria-label="Photo of a wire basket with books and a coffee cup on a white table"></div>
    <div class="rpp-band"></div>
    <div class="rpp-text">Research<br>Policy<br>Practice</div>
    <div class="rpp-circle"></div>
  </section>

  <section class="slide col-a row-2">
    <div class="photo welcome-photo" role="img" aria-label="Black and white photo of a teacher and cheering students in a classroom"></div>
    <div class="welcome-box">WELCOME</div>
    <div class="welcome-brand"><div class="brand"><span class="brand-dot"></span>KL7ux</div></div>
  </section>

  <section class="slide col-b row-2">
    <div class="header-bar">About KL7ux</div>
    <div class="header-brand"><div class="brand"><span class="brand-dot"></span>KL7ux</div></div>
    <div class="about-text body-text">
      <p>KL7ux is a leading research organization that seeks to improve system processes and outcomes through an engaging approach to practice and implementation design.</p>
      <p>KL7ux, LLC. has unique capabilities around the research project management being proposed by the pilot demonstration project for virtual learning. The staff at KL7ux is comprised of several aspects that range from policy, practice, process, and technical. First, from the policy standpoint, Dr. Delane represents 25 years in public education. Dr. Delane has worked in various states to develop integrated virtual learning programs. Dr. Delane has help establish statewide virtual systems focused on career and college readiness in Alabama, West Virginia, Indiana, New York, Mississippi, Kentucky, Louisiana, Oregon, and Texas. His policy work has been directly related to career and college readiness in K12 schools. He has his Ed.D from Brookfield University where he focused his research on Individual Career Programs and defining Career and College Readiness.</p>
    </div>
  </section>

  <section class="slide col-a row-3">
    <div class="header-bar">Leadership Team</div>
    <div class="header-brand"><div class="brand"><span class="brand-dot"></span>KL7ux</div></div>
    <div class="lead-panel"></div>
    <div class="photo lead-photo" role="img" aria-label="Portrait photo of the principal in academic dress"></div>
    <div class="lead-name">Dr. Marcus Delane, Principal</div>
    <div class="lead-text">
      <p>I have personally spent over 20 years working in the publishing and ed tech business and have come to the conclusion that educators need a true buyer's agent, one that isn't beholding to one solution but to a solution that works for your school and your learners. I have managed over $200 Million in contracts during my time in the education publishing and ed tech business world, and now I want to provide an equitable and managed solution for schools, teachers, and ultimately the learner.</p>
      <p style="margin-top:5px">Let KL7ux help you by putting you in control with a detailed analysis, reporting, and cost analysis that can be done in a matter of weeks. We look forward to hearing from you and working with your school and/or district to ensure the best possible solution for your teachers and learners.</p>
    </div>
  </section>

  <section class="slide col-b row-3">
    <div class="header-bar">Our Services</div>
    <div class="header-brand"><div class="brand"><span class="brand-dot"></span>KL7ux</div></div>
    <div class="service" style="top:33px">
      <div class="service-icon"><svg width="11" height="9" viewBox="0 0 11 9"><path d="M1 1h4l.5.6L6 1h4v7H6l-.5.6L5 8H1z" fill="none" stroke="#fff" stroke-width="1"/></svg></div>
      <div><div class="service-title">Actionable Research</div><div class="service-text">We provide actionable research, both qualitative and quantitative, to support education initiatives and priorities. KL7ux primarily specializes in : K- 12 Education, Post Secondary and Business and Industry</div></div>
    </div>
    <div class="service" style="top:76px">
      <div class="service-icon"><svg width="11" height="10" viewBox="0 0 11 10"><g fill="#fff"><circle cx="5.5" cy="2" r="1.4"/><circle cx="2" cy="8" r="1.4"/><circle cx="9" cy="8" r="1.4"/></g><path d="M5.5 3v2.5M2 6.5V5.5h7v1" stroke="#fff" stroke-width=".8" fill="none"/></svg></div>
      <div><div class="service-title">Ed Policy &amp; Leadership</div><div class="service-text">KL7ux takes current education government policy and gathers evidence of effectiveness to bring change elements to consideration when implementing target initiatives.</div></div>
    </div>
    <div class="service" style="top:119px">
      <div class="service-icon"><svg width="11" height="9" viewBox="0 0 11 9"><rect x=".5" y=".5" width="10" height="8" fill="none" stroke="#fff"/><path d="M2 6l2.5-2.5 2 1.5L9 2.5" fill="none" stroke="#fff" stroke-width=".9"/></svg></div>
      <div><div class="service-title">Practice / Implementation Analysis</div><div class="service-text">From early childhood education to college &amp; career readiness, quality instruction and improvement begins with the strengths in teaching and learning.</div></div>
    </div>
    <div class="service" style="top:160px">
      <div class="service-icon"><svg width="10" height="10" viewBox="0 0 10 10"><circle cx="5" cy="5" r="4.2" fill="none" stroke="#fff"/><path d="M5 2.5l.8 1.7 1.8.2-1.3 1.2.4 1.8L5 6.5l-1.7.9.4-1.8-1.3-1.2 1.8-.2z" fill="#fff"/></svg></div>
      <div><div class="service-title">Negotiation Buying &amp; Review</div><div class="service-text">KL7ux is committed to helping you, the educator, make informed buying decisions based on local control and independent reviews through a simple, impartial and an effective approach.</div></div>
    </div>
  </section>

  <section class="slide col-a row-4">
    <div class="header-bar">KL7ux Overview</div>
    <div class="header-brand"><div class="brand"><span class="brand-dot"></span>KL7ux</div></div>
    <div class="overview-text body-text">
      <p>From early childhood education to college &amp; career readiness, quality instruction and improvement begins with the strengths in teaching and learning. We take the best of education research and the alignment of government policy to guide and inform priority initiatives and evaluate best practices across the country. Programmatic implementation should be determined based on analysis from empirical data, implementation successes and peer reviewed data points. KL7ux informs organizational efforts based on these principals and assists in the program/implementation analysis.</p>
      <p>KL7ux supports Local Control by valuing the input and feedback from teachers, students and community to identify the right resources that's best for schools and classrooms in the district.</p>
      <p>KL7ux is committed to helping you, the educator, make informed buying decisions based on local control and independent reviews through a simple, impartial and highly effective approach.</p>
    </div>
    <div class="photo ov-library" role="img" aria-label="Photo of students studying in a large library reading hall"></div>
    <div class="photo ov-teacher" role="img" aria-label="Photo of a teacher leading a lesson"></div>
    <div class="photo ov-class" role="img" aria-label="Photo of a classroom with students at desks"></div>
  </section>

  <section class="slide col-b row-4">
    <div class="header-bar">Chart Style</div>
    <div class="header-brand"><div class="brand"><span class="brand-dot"></span>KL7ux</div></div>
    <div class="chart-box">
      <svg width="198" height="137" viewBox="0 0 198 137" font-family="Lato, sans-serif">
        <text x="99" y="12" font-size="6" fill="#f4502a" text-anchor="middle">Y-Values</text>
        <g stroke="#eeeeee" stroke-width=".6">
          <line x1="8" y1="28" x2="190" y2="28"/><line x1="8" y1="50" x2="190" y2="50"/>
          <line x1="8" y1="72" x2="190" y2="72"/><line x1="8" y1="94" x2="190" y2="94"/>
          <line x1="8" y1="116" x2="190" y2="116"/>
        </g>
        <g fill="#c4c4c4">
          <rect x="14" y="81" width="36" height="45"/>
          <rect x="61" y="72" width="36" height="54"/>
          <rect x="109" y="55" width="36" height="71"/>
          <rect x="157" y="35" width="36" height="91"/>
        </g>
        <g font-size="4.5" fill="#f4502a" text-anchor="middle">
          <text x="32" y="87">2.7</text><text x="79" y="78">3.2</text>
          <text x="127" y="61">4.2</text><text x="175" y="41">5.3</text>
          <text x="32" y="132">Point A</text><text x="79" y="132">Point B</text>
          <text x="127" y="132">Point C</text><text x="175" y="132">Point D</text>
        </g>
      </svg>
    </div>
    <div class="points">
      <div class="point"><div class="point-title">Point A</div><div class="point-text">Lorem ipsum dolor sit amet, consectetur adipiscing elit, sed do eiusmod tempor incididunt ut labore et dolore magna aliqua</div></div>
      <div class="point"><div class="point-title">Point B</div><div class="point-text">Lorem ipsum dolor sit amet, consectetur adipiscing elit, sed do eiusmod tempor incididunt ut labore et dolore magna aliqua</div></div>
      <div class="point"><div class="point-title">Point C</div><div class="point-text">Lorem ipsum dolor sit amet, consectetur adipiscing elit, sed do eiusmod tempor incididunt ut labore et dolore magna aliqua</div></div>
      <div class="point"><div class="point-title">Point D</div><div class="point-text">Lorem ipsum dolor sit amet, consectetur adipiscing elit, sed do eiusmod tempor incididunt ut labore et dolore magna aliqua</div></div>
    </div>
  </section>

  <section class="slide col-a row-5">
    <div class="header-bar">Public Research</div>
    <div class="header-brand"><div class="brand"><span class="brand-dot"></span>KL7ux</div></div>
    <div class="study" style="left:15px">
      <svg width="30" height="38" viewBox="0 0 30 38"><path d="M15 37C6 27 1 21 1 14a14 14 0 0 1 28 0c0 7-5 13-14 23z" fill="#f4502a"/><circle cx="15" cy="14" r="10" fill="#fff"/><g fill="#f4502a"><circle cx="12" cy="10.5" r="1.8"/><circle cx="18" cy="10.5" r="1.8"/><path d="M9.5 19l1-6h3l1 6zM15.5 19l1-6h3l1 6z"/></g></svg>
      <div class="study-title">Summary of Impact of Early Childhood Research</div>
      <ul class="study-list"><li>Story Garden Library Research / Literature Review</li><li>SGL Research Summary</li></ul>
    </div>
    <div class="study" style="left:96px">
      <svg width="30" height="38" viewBox="0 0 30 38"><path d="M15 37C6 27 1 21 1 14a14 14 0 0 1 28 0c0 7-5 13-14 23z" fill="#f4502a"/><circle cx="15" cy="14" r="10" fill="#fff"/><path d="M9 10h5l1 1 1-1h5v8h-5l-1 1-1-1H9z" fill="#f4502a"/></svg>
      <div class="study-title">Early College High School Research</div>
      <ul class="study-list"><li>Riverbend Early College High School: Consolidated Report</li><li>Riverbend Early College High School: The High School Perspective</li><li>Riverbend Early College High School: The College and University Perspective</li><li>Riverbend Early College High School: The Business and Community Organization Perspective</li></ul>
    </div>
    <div class="study" style="left:178px">
      <svg width="30" height="38" viewBox="0 0 30 38"><path d="M15 37C6 27 1 21 1 14a14 14 0 0 1 28 0c0 7-5 13-14 23z" fill="#f4502a"/><circle cx="15" cy="14" r="10" fill="#fff"/><path d="M11 8h6l3 3v8h-9z" fill="#f4502a"/><path d="M13 15l2 1.5 3-3.5" stroke="#fff" stroke-width=".9" fill="none"/></svg>
      <div class="study-title">Open Pathways: Increasing Social Capital in Rural Regions</div>
      <ul class="study-list"><li>Developing an understanding of what conditions are necessary for student agency to have an impact on community vitality</li><li>Increasing Social Capital in Rural Regions: Executive Summary</li></ul>
    </div>
    <div class="study" style="left:259px">
      <svg width="30" height="38" viewBox="0 0 30 38"><path d="M15 37C6 27 1 21 1 14a14 14 0 0 1 28 0c0 7-5 13-14 23z" fill="#f4502a"/><circle cx="15" cy="14" r="10" fill="#fff"/><circle cx="15" cy="12.5" r="3.8" fill="#f4502a"/><rect x="13" y="16.5" width="4" height="2.5" fill="#f4502a"/></svg>
      <div class="study-title">Early Innovation Research Abstracts</div>
      <ul class="study-list"><li>Harlow Valley Simulated Workplace</li><li>Pathways 2.0</li><li>Riverbend State Innovation Lab</li><li>The 5+2 Ready for College</li><li>Bringing Learners Home to Learning (BLHL)</li></ul>
    </div>
  </section>

  <section class="slide col-b row-5">
    <div class="header-bar">Contact Us</div>
    <div class="contact-brand"><div class="brand"><span class="brand-dot"></span>KL7ux</div></div>
    <div class="contact-row" style="top:96px">
      <svg width="10" height="13" viewBox="0 0 10 13"><path d="M5 12.5C2 9 .5 6.8.5 4.8a4.5 4.5 0 0 1 9 0c0 2-1.5 4.2-4.5 7.7z" fill="#f4502a"/><circle cx="5" cy="4.8" r="1.7" fill="#fff"/></svg>
      <div>418 Linden Avenue, Suite 210<br>Harlow, OR 97120</div>
    </div>
    <div class="contact-row" style="top:123px">
      <svg width="10" height="13" viewBox="0 0 10 13"><rect x=".5" y=".5" width="9" height="12" rx="1" fill="#f4502a"/><g fill="#fff"><rect x="2" y="2" width="6" height="3"/><rect x="2" y="6.5" width="1.5" height="1.5"/><rect x="4.25" y="6.5" width="1.5" height="1.5"/><rect x="6.5" y="6.5" width="1.5" height="1.5"/><rect x="2" y="9" width="1.5" height="1.5"/><rect x="4.25" y="9" width="1.5" height="1.5"/><rect x="6.5" y="9" width="1.5" height="1.5"/></g></svg>
      <div>555.014.0199</div>
    </div>
    <div class="contact-row" style="top:151px">
      <svg width="12" height="9" viewBox="0 0 12 9"><rect x=".5" y=".5" width="11" height="8" fill="#f4502a"/><path d="M.8 .8L6 5l5.2-4.2" stroke="#fff" stroke-width=".9" fill="none"/></svg>
      <div>mdelane@kl7ux.example</div>
    </div>
  </section>

</div>
</body>
</html>
```